BRANTLEY SKY FESTIVAL JULY 2017

INVITATION TO MEDICAL LECTURE AT BRANTLEY SKYFESTIVAL 2017, JULY 25TH, THIS WILL BE MAILED TO APPROX 750 AVIATION MEDICAL EXAMINERS, MDS.

Target Market(s)

Aviation Medical Examiners

Industry/Entity Type

Medical

Colors
ec1f27
3377b5

Requirements
Must have
• Front of postcard: Art to include Airplane, Medical / Staff of Medicine Icon,
• Back of postcard:
• GO BEYOND STANDARD LIPID TESTING AND IMPROVE CARDIAC RISK:
• BRANTLEY SKY FESTIVAL 2017, TUESDAY JULY 25th, MORLAND THEATRE
• 8:00-9:00 am “CODE BLUE AT 40,000 FEET” DR. THOMAS HALVERD
• 9:00-10:00 am “VERY HIGH RISK GROUPS WITH CORONARY HEART DISEASE, A NATIONAL EMERGENCY” DR. WALTER DANNIMOR
• 10:00-11:00 am “BEYOND CHOLESTEROL, THE NEED FOR ADVANCED LIPIDS, APPLICATION TO PILOTS” DR. WALTER DANNIMOR
• 11:00-12:00 am “PROTECTING THE COCKPIT, PILOTS AND UNDETECTED HEART DISEASE” DR. MARTIN COLVERY
• 1:00-2:00 am “PERSONAL LIFESTYLE MODIFICATIONS TO DECREASE HEART DISEASE” JUNE FARROW, NP
• RSVP: Caroline Whitfield 508-462-817
Nice to have
• ON BACK all info above to list medical presentations, Cardiac Heart Icon, (heart with rhythm logo), on left, address to attendee on the right
• ON FRONT: Color POP with AVIATION THEME
Should not have
• Fancy Font, (please keep it clean and simple, easy to read)

```html
<!DOCTYPE html>
<html lang="en">
<head>
<meta charset="utf-8">
<title>Brantley Sky Festival 2017 – Medical Lecture Postcard</title>
<link rel="stylesheet" href="https://fonts.googleapis.com/css2?family=Open+Sans:wght@400;600;700&family=Oswald:wght@600;700&family=Roboto+Condensed:wght@700&display=swap">
<style>
  :root {
    --red: #ec1f27;
    --blue: #3377b5;
    --blue-deep: #2a63a8;
    --ink: #3b3b3b;
    --paper: #ffffff;
    --panel: #f1f1f2;
    --stage: #2b2b2d;
    --sky-top: #a9c6e2;
    --sky-low: #dfe6ee;
    --tarmac: #8c8f93;
  }
  * { margin: 0; padding: 0; box-sizing: border-box; }
  html, body { width: 864px; height: 1200px; overflow: hidden; background: var(--stage); }
  body { position: relative; font-family: "Open Sans", Arial, sans-serif; }

  .postcard {
    position: absolute;
    left: 46px;
    width: 803px;
    height: 547px;
    transform: scale(0.96);
    transform-origin: top left;
    overflow: hidden;
    background: var(--paper);
  }
  .postcard--front { top: 42px; }
  .postcard--back { top: 622px; }

  /* ---------- front ---------- */
  .hero-photo {
    position: absolute; inset: 0;
    background: linear-gradient(180deg, var(--sky-top) 0%, var(--sky-low) 52%, #c7cacd 62%, var(--tarmac) 100%);
  }
  .swoosh { position: absolute; inset: 0; width: 100%; height: 100%; }
  .front-copy {
    position: absolute; right: 48px; top: 36px;
    text-align: right; font-weight: 700; line-height: 1;
  }
  .event-title {
    font-family: "Oswald", "Arial Narrow", sans-serif;
    font-size: 37px; color: var(--red); letter-spacing: 0.2px;
    -webkit-text-stroke: 1px #fff;
    text-shadow: 2px 2px 0 #8a1015, 3px 3px 3px rgba(0,0,0,.35);
  }
  .event-date { margin-top: 20px; font-size: 30px; color: var(--blue); }
  .event-date .accent { color: var(--red); }
  .event-venue { margin-top: 14px; font-size: 30px; color: var(--ink); }
  .invite-small { margin-top: 28px; font-size: 31px; color: var(--red); }
  .invite-large { margin-top: 4px; font-size: 45px; color: var(--red); }

  /* ---------- back ---------- */
  .back-shapes { position: absolute; inset: 0; width: 100%; height: 100%; }
  .program-heading {
    position: absolute; left: 0; top: 29px; width: 450px; height: 52px;
    background: var(--blue); color: #fff;
    font-size: 15px; font-weight: 600; line-height: 22px;
    padding: 4px 0 0 46px;
  }
  .program {
    position: absolute; left: 40px; top: 98px; width: 420px; list-style: none;
    font-size: 12.4px; font-weight: 700; line-height: 17px; color: var(--ink);
  }
  .program li { position: relative; padding-left: 25px; margin-bottom: 9px; }
  .program li.narrow { width: 228px; margin-bottom: 10px; }
  .program .tick { position: absolute; left: 0; top: 2px; width: 14px; height: 14px; }
  .program .talk { color: var(--red); }
  .heart-icon { position: absolute; left: 505px; top: 50px; width: 126px; height: 92px; }
  .stamp-box { position: absolute; left: 655px; top: 48px; width: 99px; height: 99px; border: 1px solid #8d8d8d; }
  .venue-address {
    position: absolute; left: 40px; top: 466px;
    font-size: 14px; line-height: 22px; color: var(--red); padding-left: 18px;
  }
  .venue-address .pin { position: absolute; left: 0; top: 3px; width: 11px; height: 15px; }
  .rsvp {
    position: absolute; left: 384px; top: 458px; height: 52px; width: 98px;
    color: #fff; text-align: center; font-weight: 700;
  }
  .rsvp-word { display: block; font-size: 28px; line-height: 32px; }
  .rsvp-note { display: block; font-size: 10px; line-height: 12px; }
  .rsvp-name {
    position: absolute; left: 486px; top: 466px;
    color: #fff; font-size: 14px; font-weight: 600; line-height: 17px;
  }
  .rsvp-phone {
    position: absolute; left: 602px; top: 466px;
    font-family: "Roboto Condensed", "Arial Narrow", sans-serif;
    font-size: 29px; font-weight: 700; color: #fff; line-height: 36px;
  }
</style>
</head>
<body>

<section class="postcard postcard--front">
  <div class="hero-photo" role="img" aria-label="Photo: a doctor in a white coat showing a tablet to an airline pilot in front of a parked jet on an airfield"></div>
  <svg class="swoosh" viewBox="0 0 803 547" preserveAspectRatio="none" aria-hidden="true">
    <path d="M0,0 H255 C160,60 60,170 0,330 Z" fill="var(--blue)"/>
    <path d="M255,0 H275 C170,70 70,190 0,345 V330 C60,170 160,60 255,0 Z" fill="#fff"/>
    <path d="M275,0 H298 C185,80 80,205 0,365 V345 C70,190 170,70 275,0 Z" fill="var(--red)"/>
    <path d="M803,547 H628 C700,470 760,400 803,270 Z" fill="var(--blue)"/>
    <path d="M628,547 H610 C690,465 750,390 803,255 V270 C760,400 700,470 628,547 Z" fill="#fff"/>
    <path d="M803,547 H660 C720,490 770,430 803,360 Z" fill="var(--red)"/>
  </svg>
  <div class="front-copy">
    <p class="event-title">BRANTLEY SKY FESTIVAL 2017</p>
    <p class="event-date">TUESDAY, <span class="accent">25th JULY</span></p>
    <p class="event-venue">MORLAND THEATRE</p>
    <p class="invite-small">PLEASE</p>
    <p class="invite-large">JOIN US</p>
  </div>
</section>

<section class="postcard postcard--back">
  <svg class="back-shapes" viewBox="0 0 803 547" preserveAspectRatio="none" aria-hidden="true">
    <path d="M0,0 H392 C490,90 500,330 280,547 H0 Z" fill="var(--panel)"/>
    <path d="M392,0 H455 C535,110 540,350 300,547 H280 C500,330 490,90 392,0 Z" fill="var(--red)"/>
    <rect x="272" y="255" width="531" height="197" fill="#fff"/>
    <rect x="420" y="457" width="383" height="53" fill="var(--blue)"/>
    <polygon points="372,457 468,457 482,483 468,510 340,510" fill="var(--red)"/>
    <polygon points="468,457 482,457 496,483 482,510 468,510 482,483" fill="var(--blue-deep)"/>
  </svg>

  <h2 class="program-heading">GO BEYOND THE STANDARD OF CARE<br>AND IMPROVE CARDIAC RISK</h2>

  <ul class="program">
    <li><svg class="tick" viewBox="0 0 14 14"><path d="M1,7 L5,12 L13,1" fill="none" stroke="var(--blue)" stroke-width="2"/></svg>BRANTLEY SKY FESTIVAL 2017, <span class="talk">TUESDAY JULY 25th</span>,<br>MORLAND THEATRE</li>
    <li><svg class="tick" viewBox="0 0 14 14"><path d="M1,7 L5,12 L13,1" fill="none" stroke="var(--blue)" stroke-width="2"/></svg>8:00-9:00 am <span class="talk">“CODE BLUE</span> AT 40,000 FEET”<br>DR. THOMAS HALVERD</li>
    <li><svg class="tick" viewBox="0 0 14 14"><path d="M1,7 L5,12 L13,1" fill="none" stroke="var(--blue)" stroke-width="2"/></svg>9:00- 10:00 <span class="talk">“BEYOND CHOLESTEROL, THE NEED FOR ADVANCED LIPIDS, APPLICATION TO PILOTS”</span> DR. WALTER DANNIMOR</li>
    <li><svg class="tick" viewBox="0 0 14 14"><path d="M1,7 L5,12 L13,1" fill="none" stroke="var(--blue)" stroke-width="2"/></svg>10:00- 11:00 <span class="talk">“VERY HIGH RISK GROUPS WITH CORONARY<br>HEART DISEASE, A NATIONAL<br>EMERGENCY”</span><br>DR. WALTER DANNIMOR</li>
    <li class="narrow"><svg class="tick" viewBox="0 0 14 14"><path d="M1,7 L5,12 L13,1" fill="none" stroke="var(--blue)" stroke-width="2"/></svg>11:00-12:00 am <span class="talk">“PROTECTING THE COCKPIT, PILOTS AND UNDETECTED HEART DISEASE”</span><br>DR. MARTIN COLVERY</li>
    <li class="narrow"><svg class="tick" viewBox="0 0 14 14"><path d="M1,7 L5,12 L13,1" fill="none" stroke="var(--blue)" stroke-width="2"/></svg>1:00-2:00 am <span class="talk">“PERSONAL LIFESTYLE MODIFICATIONS TO DECREASE HEART DISEASE”</span><br>JUNE FARROW, NP</li>
  </ul>

  <svg class="heart-icon" viewBox="0 0 126 92" aria-hidden="true">
    <defs>
      <radialGradient id="heartShade" cx="0.4" cy="0.3" r="0.8">
        <stop offset="0" stop-color="#ff5a5f"/>
        <stop offset="1" stop-color="#c4141b"/>
      </radialGradient>
    </defs>
    <path d="M63,90 C30,66 10,48 10,27 C10,11 22,2 36,2 C48,2 57,9 63,19 C69,9 78,2 90,2 C104,2 116,11 116,27 C116,48 96,66 63,90 Z" fill="url(#heartShade)"/>
    <polyline points="0,50 44,50 50,40 56,64 62,22 68,58 73,46 78,50 126,50" fill="none" stroke="#fff" stroke-width="3" stroke-linejoin="round"/>
    <polyline points="0,50 10,50 116,50 126,50" fill="none" stroke="var(--red)" stroke-width="1.5"/>
  </svg>

  <div class="stamp-box"></div>

  <p class="venue-address">
    <svg class="pin" viewBox="0 0 11 15"><path d="M5.5,14 C2,9 1,7 1,5 A4.5,4.5 0 0 1 10,5 C10,7 9,9 5.5,14 Z" fill="none" stroke="var(--blue)" stroke-width="1.4"/><circle cx="5.5" cy="5" r="1.5" fill="var(--blue)"/></svg>
    Morland Theatre Aviation Hall,<br>1200 Harlow Road, Brantley, WI
  </p>

  <div class="rsvp"><span class="rsvp-word">RSVP</span><span class="rsvp-note">TEXT OR CALL</span></div>
  <p class="rsvp-name">CAROLINE<br>WHITFIELD</p>
  <p class="rsvp-phone">508-462-8170</p>
</section>

</body>
</html>
```